Fiber Optic Internet flyer promotion Winter 2016-2017

I am looking for a marketing flyer that will not be folded, single sided that will advertise a Fiber Optic internet promotion that we are currently running.

The design should be clean, flow well, quickly grab attention, and if a very few short seconds list what the promotion is, and direct them to contact us.

It needs to list a few features of the promotion, but does not need to be in this order and should flow well with the flyer
1.) Fiber Optic Internet
2.) 100 Mbits for $140 /month or 150 Mbits for $190 /month
3.) Free construction cost up to $10,000, limited funds available.
4.) Limited time offer. Must commit before funds run out.

(555) 274-3916, www.kelvoranet.example

Target Market(s)

Small to large business

Industry/Entity Type

Internet Service Provider

Requirements
Must have
• Eye catching appeal. Quickly convey the message of the promotion and our company name and phone number.
Should not have
• Our company is primarily a wireless ISP. This promotion is all about Fiber Optic. I do not want to draw attention to the "wireless" portion of our business with this flyer.

```html
<!DOCTYPE html>
<html lang="en">
<head>
<meta charset="utf-8">
<title>Kelvora Networks – Fiber Optic Internet</title>
<link rel="stylesheet" href="https://fonts.googleapis.com/css2?family=Oswald:wght@500;600&family=Roboto:wght@400;500&display=swap">
<style>
  :root {
    --red: #d3202f;
    --red-dark: #a5151f;
    --red-soft: rgba(214, 40, 70, 0.72);
    --navy: #26367c;
    --white: #ffffff;
    --paper: #f1f1f3;
    --page: #e9e9ec;
    --photo-deep: #0f2a6e;
    --photo-mid: #2f58b8;
    --photo-light: #5f88d8;
  }
  * { box-sizing: border-box; margin: 0; padding: 0; }
  html, body { width: 1078px; height: 1200px; overflow: hidden; background: var(--page); }
  .flyer {
    position: absolute; left: 128px; top: 20px;
    width: 822px; height: 1160px;
    background: linear-gradient(180deg, var(--white) 0%, var(--paper) 100%);
    overflow: hidden;
    font-family: "Roboto", Arial, sans-serif;
    box-shadow: 0 2px 10px rgba(0,0,0,0.15);
  }
  .brand {
    position: absolute; left: 18px; top: 96px; width: 330px;
    display: flex; align-items: center; gap: 12px;
    font-family: "Roboto", Arial, sans-serif; font-weight: 500;
    font-size: 34px; color: var(--navy); letter-spacing: 0.5px;
  }
  .brand-mark { width: 22px; height: 22px; background: var(--red); flex: none; }
  .photo {
    position: absolute; left: 0; top: 211px; width: 822px; height: 470px;
    background: radial-gradient(ellipse at 60% 45%, var(--photo-light) 0%, var(--photo-mid) 40%, var(--photo-deep) 100%);
  }
  .folds { position: absolute; inset: 0; width: 822px; height: 1160px; }
  .price {
    position: absolute; left: 0; width: 540px; height: 56px;
    background: var(--red-soft);
    font-family: "Oswald", "Arial Narrow", sans-serif; font-weight: 500;
    font-size: 45px; line-height: 56px; color: var(--white);
    padding-left: 14px; white-space: nowrap;
  }
  .price-100 { top: 268px; }
  .price-150 { top: 344px; }
  .badge { position: absolute; left: 568px; top: 392px; width: 234px; height: 234px; }
  .badge-ray {
    position: absolute; left: 34px; top: 34px; width: 166px; height: 166px;
    background: var(--red);
  }
  .badge-core {
    position: absolute; left: 25px; top: 25px; width: 184px; height: 184px;
    border-radius: 50%; background: var(--red);
    border: 2px dashed var(--white); outline: 8px solid var(--red);
    display: flex; align-items: center; justify-content: center; text-align: center;
  }
  .badge-text {
    transform: rotate(-14deg);
    font-family: "Roboto", Arial, sans-serif; font-weight: 400;
    font-size: 40px; line-height: 36px; color: var(--white);
  }
  .headline {
    position: absolute; right: 21px; top: 676px; height: 98px;
    font-family: "Oswald", "Arial Narrow", sans-serif; font-weight: 600;
    font-size: 68px; line-height: 98px; color: var(--white); white-space: nowrap;
  }
  .offer { position: absolute; left: 0; width: 822px; text-align: center; color: var(--navy); }
  .offer-lead { top: 805px; font-size: 38px; font-weight: 500; }
  .offer-amount {
    top: 852px; font-family: "Oswald", "Arial Narrow", sans-serif; font-weight: 500;
    font-size: 68px; line-height: 90px; color: var(--red);
  }
  .offer-note { top: 938px; font-size: 40px; font-weight: 500; }
  .deadline {
    position: absolute; left: 9px; top: 1004px; width: 800px; height: 74px;
    background: var(--navy); border-radius: 16px; padding: 6px;
  }
  .deadline-inner {
    height: 100%; border: 2px dotted var(--white); border-radius: 12px;
    font-family: "Oswald", "Arial Narrow", sans-serif; font-weight: 500;
    font-size: 46px; line-height: 58px; color: var(--white); text-align: center; letter-spacing: 0.3px;
  }
  .contact-bar {
    position: absolute; left: 0; top: 1096px; width: 822px; height: 64px;
    background: var(--red); color: var(--white);
    display: flex; align-items: center; justify-content: space-between;
    padding: 0 18px; font-size: 30px; font-weight: 400;
  }
  .contact-item { display: flex; align-items: center; gap: 14px; }
  .contact-item svg { width: 28px; height: 28px; }
</style>
</head>
<body>
<main class="flyer">
  <div class="photo" role="img" aria-label="Night city skyline with glowing binary code and three computer monitors on a desk"></div>

  <svg class="folds" viewBox="0 0 822 1160" aria-hidden="true">
    <polygon points="708,0 773,0 708,51" fill="var(--red-dark)"/>
    <polygon points="629,93 822,0 822,201 729,159" fill="var(--red)"/>
    <polygon points="629,93 708,51 729,159" fill="var(--red-dark)"/>
    <rect x="0" y="194" width="822" height="17" fill="var(--red)"/>
    <polygon points="0,523 190,621 0,728" fill="var(--red)"/>
    <polygon points="92,676 190,621 190,700 92,746" fill="var(--red-dark)"/>
    <rect x="137" y="676" width="685" height="98" fill="var(--red)"/>
  </svg>

  <div class="brand"><span class="brand-mark"></span>Kelvora Networks</div>

  <div class="price price-100">100 Mbits for $140 /month</div>
  <div class="price price-150">150 Mbits for $190 /month</div>

  <div class="badge">
    <div class="badge-ray" style="transform:rotate(0deg)"></div>
    <div class="badge-ray" style="transform:rotate(11.25deg)"></div>
    <div class="badge-ray" style="transform:rotate(22.5deg)"></div>
    <div class="badge-ray" style="transform:rotate(33.75deg)"></div>
    <div class="badge-ray" style="transform:rotate(45deg)"></div>
    <div class="badge-ray" style="transform:rotate(56.25deg)"></div>
    <div class="badge-ray" style="transform:rotate(67.5deg)"></div>
    <div class="badge-ray" style="transform:rotate(78.75deg)"></div>
    <div class="badge-core"><div class="badge-text">Limited<br>Time<br>Offer</div></div>
  </div>

  <h1 class="headline">FIBER OPTIC INTERNET</h1>

  <p class="offer offer-lead">Free construction cost up to</p>
  <p class="offer offer-amount">$10,000</p>
  <p class="offer offer-note">limited funds available</p>

  <div class="deadline"><div class="deadline-inner">MUST COMMIT BEFORE FUNDS RUN OUT</div></div>

  <footer class="contact-bar">
    <div class="contact-item">
      <svg viewBox="0 0 24 24" aria-hidden="true"><path fill="#fff" d="M6.6 10.8c1.4 2.8 3.8 5.1 6.6 6.6l2.2-2.2c.3-.3.7-.4 1-.2 1.1.4 2.3.6 3.6.6.6 0 1 .4 1 1V20c0 .6-.4 1-1 1C10.6 21 3 13.4 3 4c0-.6.4-1 1-1h3.5c.6 0 1 .4 1 1 0 1.3.2 2.5.6 3.6.1.3 0 .7-.2 1z"/></svg>
      <span>(555) 274-3916</span>
    </div>
    <div class="contact-item">
      <svg viewBox="0 0 24 24" aria-hidden="true" fill="none" stroke="#fff" stroke-width="1.6"><circle cx="12" cy="12" r="9.5"/><ellipse cx="12" cy="12" rx="4.2" ry="9.5"/><line x1="2.5" y1="12" x2="21.5" y2="12"/><path d="M4 7h16M4 17h16"/></svg>
      <span>www.kelvoranet.example</span>
    </div>
  </footer>
</main>
</body>
</html>
```